web hosting reseller site, E-COMMERCE FUNCTIONALITY, AND MONTHLY PAYMENT INTERGRATION

hie there , i need a web hosting reseller site , 5 pages seo friendly , responsive and mobile friendly, i have a seller domain , basic content uploaded , design theme . i will be selling web hosting packages and domain names , i will also offer web design services and development . my project is so simple , the basic pages have content submitted already ,etc HOME, ABOUT, CONTACT US, BLOG POST .
Target Market(s)
5
Industry/Entity Type
web hosting
Coding
Coded - Design and coding required
Number of Pages Required
5+ page
Requirements
Must have
- e commerce functionality, blog post, knowledge base , faq ,
Should not have
- affiliate links , subscription plugins

```html
<!DOCTYPE html>
<html lang="en">
<head>
<meta charset="utf-8">
<title>Hostvale – Web Hosting</title>
<link href="https://fonts.googleapis.com/css2?family=DM+Serif+Display&family=Roboto:wght@300;400;500;700&display=swap" rel="stylesheet">
<style>
:root{
  --blue:#0d8fd6;
  --navy:#1c2a3e;
  --ink:#1e2530;
  --text:#3a3f47;
  --muted:#6b7079;
  --sky:#c9e9f5;
  --pale:#e7f4fb;
  --line:#d9dde2;
  --white:#fff;
  --footer:#1f2a3c;
  --denim:#3f86c4;
  --denim-deep:#2a67a6;
}
*{box-sizing:border-box;margin:0;padding:0}
html,body{width:1200px;height:3937px;overflow:hidden}
body{position:relative;font-family:'Roboto',sans-serif;color:var(--text);background:var(--white)}
.abs{position:absolute}
.serif{font-family:'DM Serif Display',serif;color:var(--ink)}
.bar{width:60px;height:3px;background:var(--blue)}
.btn{position:absolute;background:var(--blue);color:#fff;font-weight:500;display:flex;align-items:center;justify-content:center;border-radius:3px}

/* top bar */
.topbar{position:absolute;left:0;top:0;width:1200px;height:35px;background:#f3f3f3;font-size:14px;color:var(--text)}
.topbar span{position:absolute;top:10px;display:flex;align-items:center;gap:8px}
.social{position:absolute;top:11px;width:13px;height:13px;border-radius:50%;background:var(--navy)}
.nav{position:absolute;top:35px;left:0;width:1200px;height:72px;background:#fff}
.logo{position:absolute;left:112px;top:12px;font-size:46px;font-weight:300;color:var(--navy);letter-spacing:-1px}
.nav a{position:absolute;top:28px;font-size:16px;color:var(--ink);text-decoration:none}
.nav a.active{color:var(--blue)}

/* hero */
.hero{position:absolute;top:107px;left:0;width:1200px;height:618px;background:var(--sky);overflow:hidden}
.hero p{position:absolute;left:112px;top:321px;width:500px;font-size:16.5px;line-height:30px;color:var(--ink)}
.hero-photo{position:absolute;left:680px;top:88px;width:420px;height:530px;border-radius:210px 210px 0 0;background:linear-gradient(180deg,#9fd3ee 0%,var(--denim) 55%,var(--denim-deep) 100%)}

/* services */
.cards{position:absolute;left:112px;top:1011px;width:977px;display:grid;grid-template-columns:repeat(5,177px);gap:21px 23px}
.card{height:151px;border:1px solid var(--line);border-radius:6px;display:flex;flex-direction:column;align-items:center;justify-content:center;gap:14px;font-size:15px;color:var(--ink);text-align:center;line-height:20px}
.card.raised{box-shadow:0 4px 16px rgba(0,0,0,.12);border-color:transparent}

/* about */
.about{position:absolute;top:1425px;left:0;width:1200px;height:561px;background:var(--pale);overflow:hidden}

/* reviews */
.review{position:absolute;top:2283px;width:469px;height:234px;background:#fff;box-shadow:0 4px 18px rgba(0,0,0,.12)}
.avatar{position:absolute;left:22px;top:20px;width:96px;height:96px;border-radius:50%;background:linear-gradient(160deg,#c9d6e2,#8fa6bd);border:3px solid #e8e8e8}
.review .who{position:absolute;left:146px;top:42px;font-size:17px;color:var(--blue)}
.stars{position:absolute;left:146px;top:68px;color:#f3b41b;font-size:15px;letter-spacing:1px}
.quote{position:absolute;right:28px;top:30px;font-family:'DM Serif Display',serif;font-size:110px;line-height:1;color:#e2e2e2}
.review p{position:absolute;left:28px;top:136px;width:420px;font-size:15px;line-height:28px;color:var(--ink)}
.review i{position:absolute;right:0;bottom:0;width:21px;height:18px;background:#a9a9a9}

/* guarantee */
.guarantee{position:absolute;left:112px;top:2607px;width:977px;height:270px;border-radius:46px;background:linear-gradient(120deg,#0d8fd6,#0a7fc4)}

/* faq */
.faq{position:absolute;left:231px;width:738px;border:1.5px solid var(--line);border-radius:6px;background:#fff}
.faq h4{position:absolute;left:27px;top:24px;font-size:16px;font-weight:400;color:var(--ink)}
.faq .sign{position:absolute;right:30px;top:18px;font-size:30px;font-weight:300;color:var(--blue)}
.faq.open{border-color:var(--blue)}
.faq p{position:absolute;left:27px;top:71px;width:680px;font-size:16px;line-height:30px;color:var(--muted)}

/* footer */
.footer{position:absolute;top:3587px;left:0;width:1200px;height:350px;background:var(--footer);color:#fff}
.footer h5{position:absolute;top:82px;font-size:14.5px;font-weight:500;letter-spacing:.3px}
.footer h5::after{content:"";position:absolute;left:0;top:26px;width:65px;height:1px;background:#4a5568}
.footer ul{position:absolute;top:136px;list-style:none;font-size:15px;line-height:30px}
.fline{position:absolute;left:145px;font-size:15px;line-height:30px}
</style>
</head>
<body>

<div class="topbar">
  <span style="left:110px">
    <svg width="15" height="15" viewBox="0 0 24 24" fill="none" stroke="#333" stroke-width="2"><path d="M5 3h4l2 5-3 2a12 12 0 0 0 6 6l2-3 5 2v4a2 2 0 0 1-2 2A17 17 0 0 1 3 5a2 2 0 0 1 2-2z"/></svg>
    +1800-555-0142</span>
  <span style="left:268px;top:0;width:1px;height:35px;background:#ccc"></span>
  <span style="left:298px">
    <svg width="18" height="14" viewBox="0 0 24 18" fill="none" stroke="#333" stroke-width="2"><rect x="1" y="1" width="22" height="16"/><path d="M1 1l11 9 11-9"/></svg>
    info@hostvale.com</span>
  <i class="social" style="left:964px"></i>
  <i class="social" style="left:1003px"></i>
  <i class="social" style="left:1039px"></i>
  <i class="social" style="left:1074px"></i>
</div>

<header class="nav">
  <div class="logo">hostvale</div>
  <a class="active" style="left:402px">Home</a>
  <a style="left:494px">About</a>
  <a style="left:586px">Services</a>
  <a style="left:697px">Client Reviews</a>
  <a style="left:855px">Contact</a>
  <div class="btn" style="left:956px;top:9px;width:133px;height:52px;font-size:16px">Start Building</div>
</header>

<section class="hero">
  <div class="serif abs" style="left:112px;top:130px;font-size:50px">Welcome To</div>
  <div class="abs" style="left:392px;top:174px;width:90px;height:2px;background:var(--navy)"></div>
  <div class="serif abs" style="left:110px;top:178px;font-size:108px;line-height:1.1">Hostvale</div>
  <p>We believe in a world where people have the freedom to choose how their digital content is shared, and we foster their success by providing an open web platform of choice.</p>
  <div class="btn" style="left:112px;top:423px;width:142px;height:52px;font-size:16px">Host Your Site</div>
  <svg class="abs" style="left:690px;top:90px" width="510" height="528">
    <circle cx="260" cy="340" r="260" fill="none" stroke="#1b6fa3" stroke-width="1.5"/>
    <circle cx="270" cy="390" r="240" fill="var(--blue)"/>
    <circle cx="300" cy="100" r="100" fill="#8fcdec"/>
  </svg>
  <div class="hero-photo" role="img" aria-label="Smiling woman in glasses and a denim shirt holding an open laptop"></div>
</section>

<section>
  <div class="serif abs" style="left:0;top:780px;width:1200px;text-align:center;font-size:52px">Our Services</div>
  <div class="bar abs" style="left:570px;top:857px"></div>
  <p class="abs" style="left:142px;top:885px;width:916px;text-align:center;font-size:16.5px;line-height:30px;color:var(--ink)">Free SSL Access Management eCommerce Optimization Free Migration Backups Edgeguard CDN &amp; DDoS Protection SwiftServe SitePress Module One-Click SitePress Installation 24/7/365 Tech Support Auto Script Installer 99.9% Uptime Guarantee</p>
  <div class="cards">
    <div class="card raised"><svg width="60" height="60"><circle cx="24" cy="24" r="20" fill="#1bc4b4"/><rect x="30" y="28" width="26" height="26" rx="3" fill="#4a6d9a"/></svg>Web Hosting</div>
    <div class="card"><svg width="60" height="60"><circle cx="30" cy="30" r="28" fill="#1c5f8c"/></svg>SitePress Hosting</div>
    <div class="card"><svg width="70" height="46"><rect x="3" y="4" width="64" height="38" rx="6" fill="#9b5c8f"/></svg>ShopCart<br>Hosting</div>
    <div class="card"><svg width="64" height="64"><circle cx="32" cy="16" r="12" fill="#3aa5dd"/><circle cx="32" cy="18" r="6" fill="#f2b21b"/><path d="M32 30v10M14 40h36M14 40v6M32 40v6M50 40v6" stroke="#334" stroke-width="2" fill="none"/><circle cx="14" cy="52" r="7" fill="#2d7fc1"/><circle cx="32" cy="52" r="7" fill="#2d7fc1"/><circle cx="50" cy="52" r="7" fill="#2d7fc1"/></svg>Reseller Hosting</div>
    <div class="card"><svg width="60" height="60"><rect x="2" y="4" width="56" height="14" rx="3" fill="#2d7fc1"/><rect x="2" y="22" width="56" height="14" rx="3" fill="#2d7fc1"/><path d="M6 50h48" stroke="#2d7fc1" stroke-width="3"/><circle cx="30" cy="50" r="5" fill="#2d7fc1"/></svg>Cloud Hosting</div>
    <div class="card"><svg width="56" height="56"><rect x="2" y="4" width="52" height="50" rx="3" fill="#dde3f0"/><rect x="2" y="4" width="52" height="10" fill="#e2574c"/><g font-size="9" fill="#334" font-family="Roboto,sans-serif"><text x="14" y="28">.COM</text><text x="14" y="38">.NET</text><text x="14" y="48">.INFO</text></g></svg>Domain Names</div>
    <div class="card"><svg width="60" height="60"><rect x="2" y="4" width="56" height="14" rx="2" fill="#2d7fc1"/><rect x="2" y="22" width="56" height="14" rx="2" fill="#2d7fc1"/><rect x="2" y="40" width="56" height="14" rx="2" fill="#2d7fc1"/><path d="M30 18l12 5v10c0 8-6 13-12 16-6-3-12-8-12-16V23z" fill="#6abf4b"/></svg>Dedicated hosting</div>
    <div class="card"><svg width="60" height="60"><rect x="6" y="6" width="48" height="36" rx="3" fill="#2d7fc1"/><rect x="11" y="11" width="38" height="26" fill="#e8eef6"/><rect x="24" y="42" width="12" height="10" fill="#334"/><rect x="16" y="52" width="28" height="4" fill="#e2574c"/></svg>Site Builder</div>
    <div class="card"><svg width="60" height="64"><path d="M30 2l26 10v20c0 16-12 26-26 30C16 58 4 48 4 32V12z" fill="#7cc576"/><text x="30" y="26" text-anchor="middle" fill="#fff" font-size="16" font-weight="700" font-family="Roboto,sans-serif">SSL</text><rect x="23" y="36" width="14" height="11" rx="2" fill="#fff"/></svg>SSL</div>
    <div class="card"><svg width="60" height="60"><rect x="8" y="4" width="40" height="14" rx="2" fill="#6a4fa0"/><rect x="8" y="22" width="40" height="14" rx="2" fill="#6a4fa0"/><rect x="8" y="40" width="40" height="14" rx="2" fill="#6a4fa0"/><circle cx="48" cy="12" r="9" fill="#3aa5dd"/></svg>Shared hosting</div>
  </div>
</section>

<section class="about">
  <svg class="abs" style="left:0;top:0" width="560" height="561">
    <circle cx="310" cy="264" r="209" fill="#b8dcee"/>
    <circle cx="112" cy="468" r="115" fill="var(--blue)"/>
  </svg>
  <div class="abs" role="img" aria-label="Desktop monitor with website design mockups fanned out beside it" style="left:30px;top:140px;width:515px;height:310px;border-radius:8px;background:linear-gradient(110deg,#e4ecf3,#7fa6d3 45%,#f2f5f9)"></div>
  <div class="serif abs" style="left:573px;top:75px;font-size:52px">About us</div>
  <div class="bar abs" style="left:573px;top:146px"></div>
  <div class="abs" style="left:573px;top:186px;font-size:18.5px;font-weight:500;color:var(--ink)">A Unique Team Behind Your Online Success</div>
  <p class="abs" style="left:573px;top:225px;width:516px;font-size:16.3px;line-height:30px">What makes Hostvale unique is our extraordinary team of individuals who put their passion, dedication, and expertise into taking care of our customers' websites. We love what we do and we are motivated to deliver an outstanding level of service.</p>
  <p class="abs" style="left:573px;top:358px;width:516px;font-size:16.3px;line-height:30px">Expert And Friendly Hosting Support Our support team is famous for being fast, friendly and helpful. Every year, our customers confirm this fact giving us many five-star reviews and satisfaction rates close to 100%.</p>
</section>

<section>
  <div class="serif abs" style="left:0;top:2038px;width:1200px;text-align:center;font-size:52px">Hostvale Web Hosting Reviews</div>
  <div class="bar abs" style="left:570px;top:2114px"></div>
  <p class="abs" style="left:140px;top:2153px;width:920px;text-align:center;font-size:16.3px;line-height:30px;color:var(--ink)">We get hundreds of five-star ratings and the quality of our service gets praised all over. Read here what real customers have to say about our hosting, why they rate our service high, and what makes us different from the rest.</p>
  <svg class="abs" style="left:36px;top:2390px" width="40" height="20"><path d="M38 10H3M12 2L3 10l9 8" stroke="#999" stroke-width="2" fill="none"/></svg>
  <svg class="abs" style="left:1122px;top:2390px" width="40" height="20"><path d="M2 10h35M28 2l9 8-9 8" stroke="var(--blue)" stroke-width="2" fill="none"/></svg>
  <div class="review" style="left:112px">
    <div class="avatar" role="img" aria-label="Customer portrait"></div>
    <div class="who">Ian, Lorem Ipsum</div>
    <div class="stars">★★★★★</div>
    <div class="quote">”</div>
    <p>Lorem ipsum dolor sit amet, consectetur adipiscing elit, sed do eiusmod tempor incididunt Lorem ipsum dolor sit amet, consectetur adised do eiusmod tempor incididunt.</p>
    <i></i>
  </div>
  <div class="review" style="left:618px">
    <div class="avatar" role="img" aria-label="Customer portrait"></div>
    <div class="who">Ian, Lorem Ipsum</div>
    <div class="stars">★★★★★</div>
    <div class="quote">”</div>
    <p>Lorem ipsum dolor sit amet, consectetur adipiscing elit, sed do eiusmod tempor incididunt Lorem ipsum dolor sit amet, consectetur adised do eiusmod tempor incididunt.</p>
    <i></i>
  </div>
</section>

<section class="guarantee">
  <div class="abs" style="left:60px;top:50px;font-family:'DM Serif Display',serif;font-size:50px;color:#fff">Money-Back Guarantee</div>
  <p class="abs" style="left:61px;top:131px;width:545px;font-size:16.5px;line-height:30px;color:#fff">Try us and love us, or get a refund within 30 days of signing up. Your satisfaction is our top priority and we're confident you'll be pleased with our services.</p>
  <div class="abs" style="left:755px;top:107px;width:145px;height:55px;border:1.5px solid #fff;border-radius:4px;color:#fff;font-size:16px;font-weight:500;display:flex;align-items:center;justify-content:center">Host Your Site</div>
</section>

<section>
  <div class="serif abs" style="left:0;top:2932px;width:1200px;text-align:center;font-size:52px">FAQ</div>
  <div class="bar abs" style="left:570px;top:3015px"></div>
  <div class="faq" style="top:3062px;height:71px"><h4>1. Sed ut perspiciatis unde omnis iste natus error sit voluptatem</h4><span class="sign">+</span></div>
  <div class="faq open" style="top:3155px;height:182px"><h4>2. Sed ut perspiciatis unde omnis iste natus error sit voluptatem</h4><span class="sign" style="top:14px">—</span>
    <p>Sed ut perspiciatis unde omnis iste natus error sit voluptatem accusantium doloremque laudantium, totam reperiam, eaque ipsa quae ab illo inventore veritatis et quasi architecto beatae vitae dicta sunt explicabo.</p></div>
  <div class="faq" style="top:3361px;height:71px"><h4>3. Sed ut perspiciatis unde omnis iste natus error sit voluptatem</h4><span class="sign">+</span></div>
  <div class="faq" style="top:3452px;height:71px"><h4>4. Sed ut perspiciatis unde omnis iste natus error sit voluptatem</h4><span class="sign">+</span></div>
  <svg class="abs" style="left:1030px;top:3412px" width="110" height="110"><path d="M110 0v100L10 0z" fill="#aebfca"/></svg>
</section>

<footer class="footer">
  <h5 style="left:110px">CONTACT US</h5>
  <svg class="abs" style="left:110px;top:136px" width="20" height="26" viewBox="0 0 20 26" fill="none" stroke="#fff" stroke-width="1.5"><path d="M10 25S2 15 2 9a8 8 0 0 1 16 0c0 6-8 16-8 16z"/><circle cx="10" cy="9" r="3"/></svg>
  <div class="fline" style="top:134px">Hostvale,<br>Address Comes Here</div>
  <svg class="abs" style="left:110px;top:210px" width="18" height="18" viewBox="0 0 24 24" fill="none" stroke="#fff" stroke-width="1.6"><path d="M5 3h4l2 5-3 2a12 12 0 0 0 6 6l2-3 5 2v4a2 2 0 0 1-2 2A17 17 0 0 1 3 5a2 2 0 0 1 2-2z"/></svg>
  <div class="fline" style="top:204px">+1800-555-0142</div>
  <svg class="abs" style="left:110px;top:256px" width="20" height="15" viewBox="0 0 24 18" fill="none" stroke="#fff" stroke-width="1.6"><rect x="1" y="1" width="22" height="16"/><path d="M1 1l11 9 11-9"/></svg>
  <div class="fline" style="top:248px">info@hostvale.com</div>

  <h5 style="left:393px">QUICK LINKS</h5>
  <ul style="left:393px"><li>Home</li><li>About</li><li>Services</li><li>Client Reviews</li><li>Contact</li></ul>

  <h5 style="left:616px">OTHER LINKS</h5>
  <ul style="left:616px"><li>Careers</li><li>Terms &amp; Services</li><li>Privacy</li><li>Blog</li></ul>

  <h5 style="left:813px">SUBSCRIBE NEWSLWTTER</h5>
  <div class="abs" style="left:815px;top:135px;width:274px;height:54px;background:#fff;border-radius:3px;color:var(--ink);font-size:16px;padding:17px 16px">Email ID</div>
  <div class="btn" style="left:815px;top:197px;width:93px;height:52px;font-size:16px">Submit</div>

  <div class="abs" style="left:110px;top:305px;width:979px;height:1px;background:#3c4759"></div>
  <div class="abs" style="left:0;top:320px;width:1200px;text-align:center;font-size:15px">2022 Hostvale. All Rights Reserved.</div>
</footer>

</body>
</html>
```